A modern, fresh introduction to Buddhism

I need a book cover for an A6 sized book to be used both for ebook and hard copy. The author is a young, modern Buddhist teacher of high standing who has written this short intro to Buddhism in an informal Q & As format using modern, accessible language to convey profound and meaningful ideas to the general public. The author is Tibetan, but teaches worldwide and is very personable and dynamic. The cover should portray this and have a fresh yet authentic feel to it (nothing new-agey!). Please see the author's websites www.torvanelmiro.org and www.wbrt.org for reference, but do not feel that the design must align completely with the website designs.

Target Market(s)

General public both in Europe and America and in Asia ranging from teenagers to the elderly. A really broad audience.

Industry/Entity Type

Teacher

Requirements
Must have
• Please include the following text that on the front cover:

A Breath of Quiet Rivers

By Venerable Tsomar Deleng

Please include the following on the back cover:

Yarkun Tselpa Publications (with attached logo above it)
Nice to have
• A simplistic, artistic, and modern look without any traditional religious images.
Should not have
• No buddha images or religious images. I would prefer a more simplistic, modern and artistic look.

```html
<!DOCTYPE html>
<html lang="en">
<head>
<meta charset="utf-8">
<title>A Breath of Quiet Rivers</title>
<link href="https://fonts.googleapis.com/css2?family=Anton&family=Roboto+Condensed:wght@400&display=swap" rel="stylesheet">
<style>
  :root {
    --mist-light: #e4e6e8;
    --mist-mid: #b9bdc0;
    --foliage: #4f5a3a;
    --foliage-dark: #2f3824;
    --saffron: #e9bf1f;
    --rule-dark: #2a2a24;
    --title-navy: #1c3a66;
    --ink: #111111;
  }
  html, body {
    margin: 0;
    padding: 0;
    overflow: hidden;
    background: #ffffff;
  }
  .cover {
    position: relative;
    width: 848px;
    height: 1200px;
    overflow: hidden;
    background: var(--saffron);
  }
  .cover-photo {
    position: absolute;
    left: 0;
    top: 0;
    width: 848px;
    height: 778px;
    background:
      linear-gradient(180deg,
        var(--mist-light) 0%,
        var(--mist-mid) 38%,
        #9ea39a 58%,
        var(--foliage) 80%,
        var(--foliage-dark) 100%);
  }
  .author {
    position: absolute;
    left: 0;
    width: 848px;
    top: 727px;
    margin: 0;
    text-align: center;
    font-family: "Roboto Condensed", sans-serif;
    font-size: 25px;
    font-weight: 400;
    color: var(--saffron);
  }
  .band-rule {
    position: absolute;
    left: 0;
    width: 848px;
    height: 8px;
    top: 786px;
    background: var(--rule-dark);
  }
  .title {
    position: absolute;
    left: 0;
    width: 848px;
    top: 898px;
    margin: 0;
    text-align: center;
    font-family: "Anton", sans-serif;
    font-weight: 400;
    font-size: 58px;
    line-height: 1;
    letter-spacing: 0.5px;
    color: var(--title-navy);
  }
  .subtitle {
    position: absolute;
    left: 0;
    width: 848px;
    top: 979px;
    margin: 0;
    text-align: center;
    font-family: "Roboto Condensed", sans-serif;
    font-weight: 400;
    font-size: 35px;
    color: var(--ink);
  }
</style>
</head>
<body>
  <main class="cover">
    <div class="cover-photo" role="img" aria-label="Strings of colourful prayer flags stretched across a misty hillside with a large tree fading into fog and green shrubs below"></div>
    <p class="author">Venerable Tsomar Deleng</p>
    <div class="band-rule"></div>
    <h1 class="title">A Breath of Quiet Rivers</h1>
    <p class="subtitle">A Short Introduction to the Buddha's Teaching</p>
  </main>
</body>
</html>
```